WP website design (Volkamp)

We need a wordpress design for an established auction and real estate company based in Kansas. The winning design will incorporate a professional color scheme with company logo in a clean layout. The design needs to consider that this will be developed on a responsive theme. Colors are blue and gray, with perhaps an accent/highlight color.

Industry/Entity Type

Real Estate

Font styles to use
Serif
Sans Serif

Colors

Designer to choose colors to be used in the design.

Requirements
Must have
• Navigation:
1) Home 2) Auctions 3) Real Estate Listings 4) Buyers 5) Sellers 6) About Us 7) Contact Us 7) Brokers

Page will have slideshow, please use any stock real estate image initially. Homepage will have auctions - as at http://brindlegavelco.example/upcoming-auctions/. Footer will have smaller company logo and attached association logos.

Widgets:
1) email sign up 2) Social media (twitter, FB, youtube, RSS) 3) News & Events blog 4) Video Player
Nice to have
• demonstrate the drop-down menu styling, Past Auctions - under the main Auctions tab

```html
<!DOCTYPE html>
<html lang="en">
<head>
<meta charset="utf-8">
<title>Crestline Country – Volkamp Auction/Realty</title>
<link rel="stylesheet" href="https://fonts.googleapis.com/css2?family=Noto+Serif:wght@400;700&family=Arimo:wght@400;700&family=Open+Sans:wght@400;600&display=swap">
<style>
:root{
  --blue:#0b4f8f;
  --blue-dark:#063a6c;
  --navy:#07335f;
  --gray-bg:#f1f1f1;
  --panel:#f4f4f4;
  --line:#d8d8d8;
  --text:#4a4a4a;
  --dark:#1f2221;
  --orange:#e9741c;
}
*{box-sizing:border-box;margin:0;padding:0}
html,body{width:1008px;height:1200px;overflow:hidden}
body{background:var(--gray-bg);font-family:"Arimo",Arial,sans-serif;color:var(--text);position:relative}
.page{position:absolute;left:68px;top:0;width:874px;height:1200px;background:#fff}
.abs{position:absolute}
.topbar{left:68px;top:0;width:874px;height:5px;background:var(--blue-dark)}
.brand{left:86px;top:18px;width:170px;text-align:center;color:var(--blue)}
.brand .main{font-family:"Noto Serif",serif;font-weight:700;font-size:25px;line-height:26px}
.brand .sub{font-family:"Open Sans",sans-serif;font-weight:600;font-size:13px;color:#555;line-height:15px;margin-top:8px}
.call{right:66px;top:17px;font-family:"Open Sans",sans-serif;font-size:11px;color:#444}
.call b{font-size:13px;font-weight:600}
.social-top{left:778px;top:74px;display:flex;gap:10px}
.dot{width:27px;height:27px;border-radius:50%;background:var(--blue);border:2px solid #dfe6ee}
.dot.rss{background:var(--orange)}
.nav{left:86px;top:117px;width:836px;height:35px;border-radius:6px;background:linear-gradient(#1565b0,var(--blue-dark));display:flex;justify-content:space-around;align-items:center;padding:0 10px}
.nav a{color:#fff;font-size:11px;font-weight:700;text-decoration:none;padding:7px 11px;border-radius:3px}
.nav a.active{background:var(--navy);border:1px solid #3a76b3}
.slider{left:92px;top:176px;width:542px;height:307px;background:#fff;border:1px solid #e3e3e3;box-shadow:0 0 4px rgba(0,0,0,.1)}
.slide{position:absolute;left:7px;top:7px;width:528px;height:291px;background:linear-gradient(#1a3a9a 0%,#3d6bc4 40%,#d8d2b8 62%,#36b6e6 80%,#1aa4e0 100%)}
.dropdown{left:168px;top:163px;width:117px;height:92px;background:#2b2b2b;border-radius:3px;padding:7px 4px;z-index:3}
.dropdown:before{content:"";position:absolute;left:51px;top:-8px;border:8px solid transparent;border-top:0;border-bottom-color:#2b2b2b}
.dropdown a{display:block;font-family:"Noto Serif",serif;font-size:11px;color:#fff;text-decoration:none;padding:4px 5px;border-bottom:1px dotted #666;height:28px;line-height:20px}
.dropdown a:last-child{border:0}
.dropdown a.on{background:#174f87}
.dropdown a:before{content:"» ";font-weight:700}
.signup{left:654px;top:175px;width:263px;height:310px;background:var(--panel);border:1px solid #e3e3e3;border-radius:8px;box-shadow:0 0 4px rgba(0,0,0,.08);padding:16px 13px}
.signup h2{font-family:"Noto Serif",serif;font-size:20px;font-weight:700;color:#555}
.signup h2 span{color:var(--blue)}
.signup p{font-size:10.5px;line-height:15px;margin:14px 0 16px;letter-spacing:.3px}
.field{height:35px;border-radius:18px;background:#ececec;border:1px solid #d4d4d4;box-shadow:inset 0 2px 3px rgba(0,0,0,.12);font-size:11px;color:#555;padding:11px 16px;margin-bottom:12px}
.btn-sub{position:absolute;right:16px;top:259px;width:127px;height:37px;border-radius:9px;background:linear-gradient(#1a6bbb,var(--blue-dark));border:2px solid #cfdbe8;color:#fff;font-family:"Open Sans",sans-serif;font-size:15px;text-align:center;line-height:33px}
.h-sec{font-family:"Noto Serif",serif;font-weight:700;font-size:21px;color:var(--blue)}
.auctions{left:86px;top:554px;width:560px;height:430px;background:var(--panel);border:1px solid #dadada;border-radius:6px;padding:0 8px}
.item{position:relative;height:143px;border-bottom:1px dashed #c6c6c6;padding-top:19px}
.item:last-child{border:0}
.thumb{position:absolute;left:5px;top:19px;width:142px;height:102px;background:#fff;border:1px solid #ddd;padding:4px}
.thumb div{width:100%;height:100%;background:linear-gradient(#3f9fd6 0%,#bfe1f0 30%,#28b3c6 55%,#e8e8e8 80%,#bfbfbf 100%)}
.info{position:absolute;left:164px;top:25px;width:380px;font-size:10.5px;line-height:15px}
.info .t{font-weight:700;color:#444}
.info .s{color:#666}
.info .l{font-weight:700;font-size:11.5px;color:#555;margin-top:10px}
.info .b{color:#222;margin-top:4px}
.details{position:absolute;right:7px;top:94px;width:99px;height:29px;border-radius:6px;background:linear-gradient(#1a6bbb,var(--blue-dark));border:2px solid #c9d7e6;color:#fff;font-weight:700;font-size:12px;line-height:25px;text-align:center}
.details svg{vertical-align:-3px;margin-right:5px}
.video{left:669px;top:553px;width:240px;height:186px;background:radial-gradient(circle at 50% 45%,#3a3a3a,#050505 75%)}
.video .ghost{position:absolute;left:0;right:0;top:48px;text-align:center;color:rgba(255,255,255,.12);font-family:"Noto Serif",serif;font-weight:700;font-size:24px;line-height:26px}
.video .play{position:absolute;left:94px;top:66px;width:52px;height:34px;background:rgba(0,0,0,.7);border-radius:4px}
.video .bar{position:absolute;left:5px;right:5px;bottom:4px;height:18px;background:linear-gradient(#fafafa,#cfcfcf);font-size:8px;color:#222;font-weight:700}
.news{left:661px;top:756px;width:248px;height:162px;background:var(--panel);border:1px solid #dadada;border-radius:6px;padding:8px 15px}
.news h2{font-family:"Noto Serif",serif;font-weight:700;font-size:20px;color:var(--blue)}
.news .tag{font-size:10.5px;color:var(--blue);text-decoration:underline;letter-spacing:.5px;margin-top:7px}
.news .pic{position:absolute;left:17px;top:66px;width:91px;height:57px;background:linear-gradient(#8ec4e4,#c9b79a 55%,#3f8db1)}
.news .det{position:absolute;left:113px;top:66px;font-size:10px;line-height:12px;color:#222}
.news .more{position:absolute;right:7px;top:130px;width:63px;height:21px;border-radius:4px;background:linear-gradient(#1a6bbb,var(--blue-dark));border:1px solid #9fb7d1;color:#fff;font-style:italic;font-size:10px;line-height:19px;text-align:center}
.social-big{left:678px;top:940px;display:flex;gap:16px}
.social-big .dot{width:40px;height:40px}
.badges{left:118px;top:1024px;width:740px;display:flex;justify-content:space-between;align-items:center}
.badge{background:#d9d9d9;border:2px solid #9c9c9c}
.footer{left:68px;top:1093px;width:874px;height:107px;background:var(--dark)}
.footer .brand{left:18px;top:22px;color:#cfcfcf}
.footer .brand .sub{color:#bcbcbc}
.flinks{position:absolute;right:14px;top:18px;text-align:right;color:#fff;font-size:10.5px;line-height:17px}
</style>
</head>
<body>
<div class="page"></div>
<div class="abs topbar"></div>

<div class="abs brand"><div class="main">Crestline Country</div><div class="sub">Volkamp<br>Auction/Realty, LLC</div></div>
<div class="abs call"><b>Call us free</b> on 0800 555 0142 &nbsp;8am to 8pm</div>
<div class="abs social-top" aria-label="Social media links"><span class="dot"></span><span class="dot"></span><span class="dot"></span><span class="dot rss"></span></div>

<nav class="abs nav">
  <a href="#">HoMe</a><a href="#" class="active">Auctions</a><a href="#">Real Estate Listings</a><a href="#">Buyers</a><a href="#">Sellers</a><a href="#">About Us</a><a href="#">Contact Us</a><a href="#">Brokers</a>
</nav>

<div class="abs slider"><div class="slide" role="img" aria-label="Slideshow photo: two-storey house at dusk with lit windows and a backyard swimming pool"></div></div>
<div class="abs dropdown"><a href="#" class="on">Current Auctions</a><a href="#">Past Auctions</a><a href="#">Online Auctions</a></div>

<form class="abs signup">
  <h2>Email <span>sign-up</span> form</h2>
  <p>Lorem ipsum dolor sit amet, consectetuer adipiscing elit. Nam</p>
  <div class="field">First Name</div>
  <div class="field">Last Name</div>
  <div class="field">Email Address</div>
  <div class="btn-sub">Subscribe Now</div>
</form>

<h2 class="abs h-sec" style="left:87px;top:516px">Current Auction</h2>
<div class="abs auctions">
  <div class="item">
    <div class="thumb"><div role="img" aria-label="Photo of a turquoise single-storey house with porch"></div></div>
    <div class="info"><div class="t">Simply dummy text of the printing and typesetting industry.</div><div class="s">Lorem Ipsum has been the industry's standard dummy text ever since the 1500s, when an unknown printer took a galley of type and scrambled.</div><div class="l">Auction start In</div><div class="b"><b>Begins:</b>&nbsp; Saturday, March 16, 2013 at 10:00 AM EDT</div></div>
    <div class="details"><svg width="13" height="13" viewBox="0 0 13 13"><circle cx="5.5" cy="5.5" r="4" fill="none" stroke="#fff" stroke-width="2"/><line x1="8.5" y1="8.5" x2="12" y2="12" stroke="#fff" stroke-width="2.2"/></svg>DETAILS</div>
  </div>
  <div class="item">
    <div class="thumb"><div role="img" aria-label="Photo of a turquoise single-storey house with porch"></div></div>
    <div class="info"><div class="t">Simply dummy text of the printing and typesetting industry.</div><div class="s">Lorem Ipsum has been the industry's standard dummy text ever since the 1500s, when an unknown printer took a galley of type and scrambled.</div><div class="l">Auction start In</div><div class="b"><b>Begins:</b>&nbsp; Saturday, March 16, 2013 at 10:00 AM EDT</div></div>
    <div class="details"><svg width="13" height="13" viewBox="0 0 13 13"><circle cx="5.5" cy="5.5" r="4" fill="none" stroke="#fff" stroke-width="2"/><line x1="8.5" y1="8.5" x2="12" y2="12" stroke="#fff" stroke-width="2.2"/></svg>DETAILS</div>
  </div>
  <div class="item">
    <div class="thumb"><div role="img" aria-label="Photo of a turquoise single-storey house with porch"></div></div>
    <div class="info"><div class="t">Simply dummy text of the printing and typesetting industry.</div><div class="s">Lorem Ipsum has been the industry's standard dummy text ever since the 1500s, when an unknown printer took a galley of type and scrambled.</div><div class="l">Auction start In</div><div class="b"><b>Begins:</b>&nbsp; Saturday, March 16, 2013 at 10:00 AM EDT</div></div>
    <div class="details"><svg width="13" height="13" viewBox="0 0 13 13"><circle cx="5.5" cy="5.5" r="4" fill="none" stroke="#fff" stroke-width="2"/><line x1="8.5" y1="8.5" x2="12" y2="12" stroke="#fff" stroke-width="2.2"/></svg>DETAILS</div>
  </div>
</div>

<h2 class="abs h-sec" style="left:669px;top:516px">Featured Video</h2>
<div class="abs video">
  <div class="ghost">Crestline Country</div>
  <div class="play"><svg width="52" height="34" viewBox="0 0 52 34"><polygon points="21,8 21,26 35,17" fill="#ddd"/></svg></div>
  <div class="bar"><svg width="230" height="18" viewBox="0 0 230 18"><polygon points="7,5 7,13 13,9" fill="#222"/><line x1="18" y1="2" x2="18" y2="16" stroke="#aaa"/><text x="24" y="12" font-size="8" font-family="Arimo" font-weight="700">00:00</text><rect x="54" y="7" width="115" height="4" rx="2" fill="#999"/><text x="178" y="12" font-size="8" font-family="Arimo" font-weight="700">00:00</text><line x1="208" y1="2" x2="208" y2="16" stroke="#aaa"/><rect x="214" y="6" width="7" height="7" fill="none" stroke="#222"/></svg></div>
</div>

<div class="abs news">
  <h2>News &amp; Events blog</h2>
  <div class="tag">ONLINE BIDDING ONLY</div>
  <div class="pic" role="img" aria-label="Photo of a rock arch on the coast"></div>
  <div class="det"><b>Saturday March 16,<br>2013 at 10:00 AM EDT</b><br><div style="margin-top:7px">Harlow Road<br>Millbrook, KS 67101</div></div>
  <div class="more">read more</div>
</div>

<div class="abs social-big" aria-label="Social media links"><span class="dot"></span><span class="dot"></span><span class="dot"></span><span class="dot rss"></span></div>

<div class="abs badges" aria-label="Association badges">
  <div class="badge" style="width:46px;height:54px"></div>
  <div class="badge" style="width:98px;height:52px"></div>
  <div class="badge" style="width:60px;height:48px"></div>
  <div class="badge" style="width:93px;height:42px"></div>
  <div class="badge" style="width:96px;height:44px"></div>
  <div class="badge" style="width:42px;height:50px"></div>
  <div class="badge" style="width:40px;height:42px"></div>
</div>

<footer class="abs footer">
  <div class="abs brand"><div class="main">Crestline Country</div><div class="sub">Volkamp<br>Auction/Realty, LLC</div></div>
  <div class="flinks">Home - Upcoming Auctions - Past Auctions - For Sale- Highlights - Contact Us<br>412 Fenwick Lane, Larkfield, KS 67001<br>1(555) 014-2290<br>Phone: 555- 019-3384,&nbsp;<br>Email: info@crestlinecountry.example</div>
</footer>
</body>
</html>
```